Trucking Company Website Design

We are working with a Trucking company in California. They provide trucking services for dirt, gravel, landscape bark, and landscape materials.

As you might imagine, there are no websites we could find for inspiration for trucking companies.

Thank you for taking the time to consider designing a website for us. We are web developers based in Stockton, CA, USA. Most of our projects go through the same process. Understanding this process may help you win a project with us. We custom-code all of our websites in-house. We don’t have any requirements as to what tools you use for your design, but we ask that you follow these guidelines.

IMAGES:
If you use any images or icons in the design, we ask that you have a link to the asset so we can purchase the image/icon. Most of the designs we submit do not have the customer’s images on them unless they have some great images. Be creative; show us the feeling you are trying to portray with your image choices. Use any royalty-free site you choose. We subscribe to Veltro and mainly use their images, but we can purchase images outside of Veltro. PLEASE NOTE: we will not submit designs to clients with watermarks on the images.

FONTS:
We ask that you identify the fonts you’re using in the design. This can be done in a message if you want. We typically use Plimsa Fonts and Veltro Fonts.

CONTENT:
We're always open to different content and ideas. We often submit designs with stock images so the client can see our vision. We typically take pictures after the website launch to use their images with our vision. Lorem Ipsum is fine for paragraphs, but we ask that you make the Headers with correct English. We want to be able to show the vision and identify the sections of the website.

INSPIRATION:
We typically add a couple of links in the brief of websites we like to help you get started in your design.

REVISIONS:
We do not often ask for revisions of the designs unless we see something in the design that may not appeal to the client. If there are slight changes that we want to make, we do that in the development process.

FEEDBACK:
We rarely give feedback on designs during the design process. We are working on many website projects and do not have the time to provide feedback. We usually respond if your request is well thought out and asks specific questions, but a note asking “feedback, please” usually goes unanswered.

```html
<!DOCTYPE html>
<html lang="en">
<head>
<meta charset="utf-8">
<title>Valecrest Materials – Trucking Services</title>
<link href="https://fonts.googleapis.com/css2?family=Saira:wght@600;700;800&family=Roboto:wght@400;500;700&display=swap" rel="stylesheet">
<style>
:root{
  --red:#e8192c;
  --red-dark:#c9101f;
  --blue:#1d74b3;
  --blue-mid:#2a86c2;
  --ink:#222;
  --muted:#555;
  --footer:#141414;
  --white:#fff;
  --gold:#f5a623;
}
*{box-sizing:border-box;margin:0;padding:0}
html,body{width:1200px;height:4615px;overflow:hidden}
body{position:relative;background:var(--white);font-family:"Roboto",Arial,sans-serif;color:var(--ink)}
.abs{position:absolute}
.display{font-family:"Saira",Arial,sans-serif;font-weight:800;letter-spacing:1px}
.btn{position:absolute;display:flex;align-items:center;justify-content:center;gap:8px;color:var(--white);font-weight:700;font-size:14px;text-transform:uppercase}
.btn .dot{width:12px;height:12px;border-radius:50%;background:var(--white);position:relative}
.btn .dot::after{content:"";position:absolute;left:4px;top:3px;border-left:5px solid currentColor;border-top:3px solid transparent;border-bottom:3px solid transparent}
.btn-red{background:var(--red)}
.btn-red .dot::after{border-left-color:var(--red)}
.btn-blue{background:var(--blue)}
.btn-blue .dot::after{border-left-color:var(--blue)}

/* header */
.brand{display:flex;align-items:center;gap:14px}
.brand-name{font-family:"Saira",Arial,sans-serif;font-weight:800;color:var(--blue);font-size:40px;line-height:36px;letter-spacing:1px}
.brand-name small{display:block;font-size:26px;line-height:30px;letter-spacing:3px}
.brand-mark{width:40px;height:40px;background:var(--red)}
.contact-item{display:flex;align-items:center;gap:12px}
.contact-icon{width:38px;height:38px;border-radius:50%;background:var(--blue);display:flex;align-items:center;justify-content:center}
.contact-label{font-size:13px;color:var(--ink)}
.contact-value{font-size:19px;color:var(--ink)}
.contact-value.strong{font-weight:700}
.nav{left:421px;top:80px;width:779px;height:42px;background:var(--red);clip-path:polygon(20px 0,100% 0,100% 100%,0 100%)}
.nav-home{left:448px;top:80px;width:86px;height:42px;background:var(--blue);clip-path:polygon(8px 0,100% 0,100% 100%,0 100%)}
.nav a{position:absolute;top:0;line-height:42px;color:var(--white);text-decoration:none;font-size:14px;transform:translateX(-50%);white-space:nowrap}

/* hero */
.hero{left:0;top:122px;width:1200px;height:591px;background:linear-gradient(180deg,#3c4a52 0%,#8a6a3c 38%,#d69a44 52%,#5b5a3a 70%,#2b2e25 100%)}
.hero-kicker{left:111px;top:268px;color:var(--white);font-size:34px}
.hero-title{left:111px;top:320px;color:var(--white);font-size:88px;line-height:78px;text-transform:uppercase}
.scroll-pill{left:585px;top:676px;width:30px;height:66px;border-radius:15px;background:var(--white);box-shadow:0 2px 6px rgba(0,0,0,.2)}

/* headings */
.h2{font-family:"Saira",Arial,sans-serif;font-weight:800;font-size:34px;letter-spacing:1px;text-transform:uppercase}
.h2 .accent{color:var(--blue)}
.center{text-align:center;left:0;width:1200px}
.para{font-size:15px;line-height:26.6px;color:var(--muted);text-align:justify}

/* about */
.about-photo{left:112px;top:814px;width:456px;height:456px;border-radius:50%;background:radial-gradient(circle at 50% 40%,#c8463a 0%,#7a2e28 45%,#2b3138 100%)}

/* carriers */
.carriers{left:0;top:1334px;width:1200px;height:627px}

/* services */
.service{top:2065px;width:256px;height:303px;color:var(--white);font-weight:700;font-size:17px}
.service .label{position:absolute;left:0;bottom:30px;width:100%;text-align:center}
.service-active{background:var(--blue-mid);text-align:center;padding:44px 22px 0}
.service-active h3{font-size:15px;font-weight:700;margin-bottom:18px}
.service-active p{font-size:12px;line-height:21px;font-weight:400}

/* overview */
.overview{left:0;top:2457px;width:1200px;height:477px;background:var(--blue-mid)}
.video{left:210px;top:2656px;width:780px;height:384px;border-radius:12px;overflow:hidden;background:linear-gradient(180deg,#8a9aa8 0%,#c79c78 40%,#5a4e46 65%,#2a2a2a 100%);box-shadow:0 10px 24px rgba(0,0,0,.3)}
.video-bar{position:absolute;left:0;bottom:0;width:100%;height:36px;background:linear-gradient(0deg,rgba(0,0,0,.6),rgba(0,0,0,0))}

/* testimonials */
.review{top:3202px;width:308px;height:228px;background:var(--white);border-radius:8px;box-shadow:0 4px 16px rgba(0,0,0,.12)}
.review .avatar{position:absolute;left:22px;top:20px;width:44px;height:44px;border-radius:50%;background:linear-gradient(135deg,#b9b2aa,#6e6a66)}
.review .name{position:absolute;left:82px;top:26px;font-size:15px;font-weight:500}
.review .when{position:absolute;left:82px;top:48px;font-size:11px;color:var(--muted)}
.review .badge{position:absolute;right:22px;top:28px;width:28px;height:28px;border-radius:50%;border:4px solid #4a8af4}
.review .stars{position:absolute;left:0;top:80px;width:100%;text-align:center;color:var(--gold);font-size:13px;letter-spacing:1px}
.review p{position:absolute;left:30px;top:108px;width:248px;text-align:center;font-size:14px;line-height:26px;color:var(--muted)}

/* partners */
.partners{left:0;top:3519px;width:1200px;height:278px;background:var(--red)}
.partner{top:3654px;width:167px;height:86px;background:var(--white);border-radius:6px;display:flex;align-items:center;justify-content:center}
.partner span{width:90px;height:26px;border-radius:4px;background:#d9d9d9}
.arrow{top:3684px;width:30px;height:30px;border-radius:50%;background:var(--white)}

/* newsletter */
.field{top:4006px;width:376px;height:40px;border:1px solid #ddd;font-size:11px;color:#888;padding:13px 18px}

/* footer */
.footer{left:0;top:4212px;width:1200px;height:352px;background:var(--footer)}
.foot-h{font-size:16px;font-weight:700;color:var(--white)}
.foot-list{list-style:none;color:var(--white);font-size:14px}
.foot-list li{height:34.7px}
.social{top:4396px;width:30px;height:30px;border-radius:50%;background:var(--white)}
.foot-contact{display:flex;align-items:center;gap:14px;color:var(--white);font-size:14px;line-height:19px}
.foot-contact .ic{flex:none;width:26px;height:26px;border-radius:50%;background:var(--white);display:flex;align-items:center;justify-content:center}
.copyright{left:0;top:4564px;width:1200px;height:51px;background:var(--red);color:var(--white);font-size:12px;text-align:center;line-height:51px}
</style>
</head>
<body>

<!-- Header -->
<header>
  <div class="abs brand" style="left:111px;top:28px">
    <div class="brand-name">VALECREST<small>MATERIALS</small></div>
    <div class="brand-mark"></div>
  </div>
  <div class="abs contact-item" style="left:563px;top:20px">
    <div class="contact-icon"><svg width="18" height="14" viewBox="0 0 18 14"><rect x="1" y="1" width="16" height="12" rx="1" fill="none" stroke="#fff" stroke-width="1.8"/><path d="M1 2l8 6 8-6" fill="none" stroke="#fff" stroke-width="1.8"/></svg></div>
    <div><div class="contact-label">Email Us</div><div class="contact-value">info@valecrestmaterials.com</div></div>
  </div>
  <div class="abs contact-item" style="left:889px;top:20px">
    <div class="contact-icon"><svg width="18" height="18" viewBox="0 0 24 24"><path fill="#fff" d="M6.6 10.8a15.1 15.1 0 0 0 6.6 6.6l2.2-2.2a1 1 0 0 1 1-.25 11.4 11.4 0 0 0 3.6.57 1 1 0 0 1 1 1V20a1 1 0 0 1-1 1A17 17 0 0 1 3 4a1 1 0 0 1 1-1h3.5a1 1 0 0 1 1 1c0 1.25.2 2.45.57 3.57a1 1 0 0 1-.25 1z"/></svg></div>
    <div><div class="contact-label">Call Us</div><div class="contact-value strong">+1 888 888 8888</div></div>
  </div>
  <div class="abs nav-home"></div>
  <nav class="abs nav" style="background:transparent;clip-path:none">
  </nav>
  <div class="abs nav"></div>
  <div class="abs nav-home"></div>
  <nav class="abs" style="left:0;top:80px;width:1200px;height:42px">
    <a class="abs" style="left:489px;top:0;line-height:42px;color:#fff;font-size:14px;transform:translateX(-50%);text-decoration:none">HOME</a>
    <a class="abs" style="left:596px;top:0;line-height:42px;color:#fff;font-size:14px;transform:translateX(-50%);text-decoration:none;white-space:nowrap">ABOUT US</a>
    <a class="abs" style="left:702px;top:0;line-height:42px;color:#fff;font-size:14px;transform:translateX(-50%);text-decoration:none">SERVICES</a>
    <a class="abs" style="left:790px;top:0;line-height:42px;color:#fff;font-size:14px;transform:translateX(-50%);text-decoration:none">BLOG</a>
    <a class="abs" style="left:897px;top:0;line-height:42px;color:#fff;font-size:14px;transform:translateX(-50%);text-decoration:none">TESTIMONIALS</a>
    <a class="abs" style="left:1031px;top:0;line-height:42px;color:#fff;font-size:14px;transform:translateX(-50%);text-decoration:none;white-space:nowrap">CONTACT US</a>
  </nav>
</header>

<!-- Hero -->
<section>
  <div class="abs hero" role="img" aria-label="Semi truck driving on a highway at sunset"></div>
  <div class="abs hero-kicker display">WELCOME TO</div>
  <h1 class="abs hero-title display">Valecrest<br>Materials</h1>
  <a class="btn btn-red" style="left:111px;top:516px;width:158px;height:45px">Get Started <span class="dot"></span></a>
  <div class="abs scroll-pill"><svg width="30" height="66" viewBox="0 0 30 66"><path d="M10 18l5-6 5 6M10 48l5 6 5-6" fill="none" stroke="#555" stroke-width="1.5"/><rect x="11" y="24" width="8" height="18" rx="4" fill="none" stroke="#555" stroke-width="1.5"/></svg></div>
</section>

<!-- About -->
<section>
  <div class="abs about-photo" role="img" aria-label="Red truck cab close-up"></div>
  <h2 class="abs h2" style="left:618px;top:852px"><span class="accent">ABOUT</span> US</h2>
  <p class="abs para" style="left:618px;top:906px;width:469px">Lorem ipsum dolor sit amet, consectetur adipiscing elit, sed do eiusmod tempor incididunt ut labore et dolore magna aliqua. Ut enim ad minim veniam, quis nostrud exercitation ullamco laboris nisi ut aliquip ex ea commodo consequat.Duis aute irure dolor in reprehenderit in voluptate velit esse cillum occaecat cupidatat non proident, fugiat nulla pariatur. Excepteur sunt in culpa qui officia deserunt mollit anim id est laborum. aute irure dolor in reprehenderit in voluptate velit esse cillum dolore eu fugiat nulla pariatur Excepteur sint occaecat cupidatat.Lorem ipsum dolor sit ameteed.</p>
  <a class="btn btn-red" style="left:618px;top:1173px;width:159px;height:45px">Learn More <span class="dot"></span></a>
</section>

<!-- Carriers -->
<section>
  <svg class="abs carriers" viewBox="0 0 1200 627" role="img" aria-label="Red semi truck with white trailer on a desert road">
    <defs>
      <linearGradient id="carrierPhoto" x1="0" y1="0" x2="0" y2="1">
        <stop offset="0" stop-color="#a7b4c2"/>
        <stop offset=".45" stop-color="#d6cbbd"/>
        <stop offset=".6" stop-color="#7a3a3a"/>
        <stop offset=".8" stop-color="#5a5550"/>
        <stop offset="1" stop-color="#3a3836"/>
      </linearGradient>
    </defs>
    <polygon points="0,0 600,81 600,538 0,627" fill="#e8192c"/>
    <polygon points="600,81 1200,0 1200,627 600,538" fill="url(#carrierPhoto)"/>
  </svg>
  <h2 class="abs h2" style="left:93px;top:1460px;color:#fff">OUR CARRIERS</h2>
  <p class="abs para" style="left:93px;top:1514px;width:450px;color:#fff">Lorem ipsum dolor sit amet, consectetur adipiscing elit, sed do eiusmod tempor incididunt ut labore et dolore magna aliqua. Ut enim ad minim veniam, quis nostrud exercitation ullamco laboris nisi ut aliquip ex ea commodo consequat.Duis aute irure dolor in reprehenderit in voluptate velit esse cillum occaecat cupidatat non proident, fugiat nulla pariatur. Excepteur sunt in culpa qui officia deserunt mollit anim id est laborum. aute irure dolor in reprehenderit in voluptate velit esse cillum dolore eu fugiat nulla pariatur Excepteur sint occaecat cupidatat.</p>
  <a class="btn btn-blue" style="left:93px;top:1778px;width:160px;height:47px">Learn More <span class="dot"></span></a>
</section>

<!-- Services -->
<section>
  <h2 class="abs h2 center" style="top:1977px"><span class="accent">OUR</span> SERVICES</h2>
  <div class="abs service" style="left:77px;background:linear-gradient(180deg,#7d8a98,#b48a64 50%,#3e3d3a)" role="img" aria-label="Tractors hauling dirt at dusk"><span class="label">Dirt</span></div>
  <div class="abs service" style="left:339px;background:linear-gradient(180deg,#6e7478,#a87a4a 45%,#2e2c2a)" role="img" aria-label="Excavator working a gravel pit"><span class="label">Gravel</span></div>
  <div class="abs service service-active" style="left:602px">
    <h3>Landscape Bark</h3>
    <p>Lorem ipsum dolor amet, consectetur adipiscing elit, seiusmod tempor incididunt ut labore et dolore magna aliqua. Ut enim ad minim veniam, quis nostrud exercitation ullamco laboris ex ea commodo consequat.</p>
    <a class="btn btn-red" style="left:62px;top:225px;width:132px;height:33px;font-size:12px">Learn More <span class="dot"></span></a>
  </div>
  <div class="abs service" style="left:863px;background:linear-gradient(180deg,#c9ccd0,#8e8a86 50%,#3a3838)" role="img" aria-label="Forklift loading pallets of landscape materials into a truck"><span class="label">Landscape Materials</span></div>
</section>

<!-- Overview video -->
<section>
  <div class="abs overview" role="img" aria-label="Trucks parked in a yard under a blue overlay"></div>
  <h2 class="abs h2 center" style="top:2538px;color:#fff;line-height:40px">OVERVIEW OF SERVICES WITH<br>CUSTOMER TESTIMONIALS</h2>
  <div class="abs video" role="img" aria-label="Orange dump truck on a gravel site">
    <div class="abs" style="left:306px;top:144px;width:96px;height:96px;border-radius:50%;border:4px solid #fff"></div>
    <svg class="abs" style="left:334px;top:168px" width="44" height="48" viewBox="0 0 44 48"><path d="M6 4l34 20-34 20z" fill="#fff"/></svg>
    <div class="abs display" style="left:417px;top:236px;color:#fff;font-size:34px;font-weight:700">Click To Play</div>
    <div class="video-bar">
      <svg class="abs" style="left:60px;top:12px" width="14" height="16" viewBox="0 0 14 16"><path d="M1 1l12 7-12 7z" fill="#fff"/></svg>
      <div class="abs" style="left:100px;top:5px;font-size:9px;color:#fff;background:#333;padding:1px 4px">01:58</div>
      <div class="abs" style="left:100px;top:19px;width:580px;height:3px;background:rgba(255,255,255,.5)"></div>
      <div class="abs" style="left:720px;top:12px;width:10px;height:10px;border-radius:50%;background:#fff"></div>
      <div class="abs" style="left:742px;top:12px;width:10px;height:10px;border:2px solid #fff"></div>
    </div>
  </div>
</section>

<!-- Testimonials -->
<section>
  <h2 class="abs h2 center" style="top:3119px"><span class="accent">WHAT OUR</span> CUSTOMERS &nbsp;SAY</h2>
  <div class="abs review" style="left:111px">
    <div class="avatar" role="img" aria-label="Customer portrait"></div>
    <div class="name">John Smith,</div><div class="when">2 days ago</div><div class="badge"></div>
    <div class="stars">★★★★★</div>
    <p>Sed ut perspiciatis unde omnis iste natus error sit voluptatem accusantium doloremque laudantium, totam rem aperiam, eaque ipsa</p>
  </div>
  <div class="abs review" style="left:446px">
    <div class="avatar" role="img" aria-label="Customer portrait"></div>
    <div class="name">John Smith,</div><div class="when">2 days ago</div><div class="badge"></div>
    <div class="stars">★★★★★</div>
    <p>Sed ut perspiciatis unde omnis iste natus error sit voluptatem accusantium doloremque laudantium, totam rem aperiam, eaque ipsa</p>
  </div>
  <div class="abs review" style="left:779px">
    <div class="avatar" role="img" aria-label="Customer portrait"></div>
    <div class="name">John Smith,</div><div class="when">2 days ago</div><div class="badge"></div>
    <div class="stars">★★★★★</div>
    <p>Sed ut perspiciatis unde omnis iste natus error sit voluptatem accusantium doloremque laudantium, totam rem aperiam, eaque ipsa</p>
  </div>
</section>

<!-- Partners -->
<section>
  <div class="abs partners" role="img" aria-label="Trucks on a road under a red overlay"></div>
  <h2 class="abs h2 center" style="top:3566px;color:#fff">OUR PARTNERS</h2>
  <div class="abs arrow" style="left:44px"><svg width="30" height="30" viewBox="0 0 30 30"><path d="M18 9l-7 6 7 6z" fill="#222"/></svg></div>
  <div class="abs partner" style="left:118px"><span></span></div>
  <div class="abs partner" style="left:317px"><span></span></div>
  <div class="abs partner" style="left:516px"><span></span></div>
  <div class="abs partner" style="left:715px"><span></span></div>
  <div class="abs partner" style="left:913px"><span></span></div>
  <div class="abs arrow" style="left:1126px"><svg width="30" height="30" viewBox="0 0 30 30"><path d="M12 9l7 6-7 6z" fill="#222"/></svg></div>
</section>

<!-- Newsletter -->
<section>
  <h2 class="abs h2 center" style="top:3878px"><span class="accent">OUR</span> NEWSLETTER</h2>
  <p class="abs center" style="top:3940px;font-size:15px;line-height:23px;color:var(--muted)">Signup for top tips on improving the efficiency of your plant equipment<br>News , Updates and promotions</p>
  <div class="abs field" style="left:213px">Name</div>
  <div class="abs field" style="left:611px">Emai</div>
  <a class="btn btn-red" style="left:509px;top:4080px;width:181px;height:45px">Subscribe Now <span class="dot"></span></a>
</section>

<!-- Footer -->
<footer>
  <div class="abs footer"></div>
  <div class="abs brand" style="left:111px;top:4296px">
    <div class="brand-name">VALECREST<small>MATERIALS</small></div>
    <div class="brand-mark"></div>
  </div>
  <div class="abs social" style="left:172px" aria-label="Social profile"></div>
  <div class="abs social" style="left:211px" aria-label="Social profile"></div>
  <div class="abs social" style="left:250px" aria-label="Social profile"></div>
  <div class="abs social" style="left:289px" aria-label="Social profile"></div>

  <div class="abs foot-h" style="left:455px;top:4288px">QUICK LINKS</div>
  <ul class="abs foot-list" style="left:455px;top:4332px">
    <li>FAQ</li><li>Terms and Conditions</li><li>Privacy Policy</li><li>Support</li><li>Sitemap</li><li>Contact Us</li>
  </ul>
  <div class="abs foot-h" style="left:668px;top:4288px">QUICK LINKS</div>
  <ul class="abs foot-list" style="left:668px;top:4332px">
    <li>Home</li><li>About Us</li><li>Services</li><li>Blog</li><li>Testimonials</li><li>Contact Us</li>
  </ul>
  <div class="abs foot-h" style="left:858px;top:4288px">CONTACT US</div>
  <div class="abs foot-contact" style="left:858px;top:4336px">
    <span class="ic"><svg width="14" height="14" viewBox="0 0 24 24"><path fill="#e8192c" d="M6.6 10.8a15.1 15.1 0 0 0 6.6 6.6l2.2-2.2a1 1 0 0 1 1-.25 11.4 11.4 0 0 0 3.6.57 1 1 0 0 1 1 1V20a1 1 0 0 1-1 1A17 17 0 0 1 3 4a1 1 0 0 1 1-1h3.5a1 1 0 0 1 1 1c0 1.25.2 2.45.57 3.57a1 1 0 0 1-.25 1z"/></svg></span>+1 888 888 8888</div>
  <div class="abs foot-contact" style="left:858px;top:4388px">
    <span class="ic"><svg width="14" height="11" viewBox="0 0 18 14"><rect x="1" y="1" width="16" height="12" rx="1" fill="#e8192c"/><path d="M1 2l8 6 8-6" fill="none" stroke="#fff" stroke-width="1.5"/></svg></span>info@valecrestmaterials.com</div>
  <div class="abs foot-contact" style="left:858px;top:4447px">
    <span class="ic"><svg width="12" height="15" viewBox="0 0 12 16"><path fill="#e8192c" d="M6 0a6 6 0 0 0-6 6c0 4.5 6 10 6 10s6-5.5 6-10a6 6 0 0 0-6-6zm0 8.2A2.2 2.2 0 1 1 6 3.8a2.2 2.2 0 0 1 0 4.4z"/></svg></span>150, Lorem ipsum dolor sit<br>amet, adipiscing elit,</div>
  <div class="abs copyright">2023 Copyright - Valecrest Materials. &nbsp;| &nbsp;All Rights Reserved &nbsp;|</div>
</footer>

</body>
</html>
```